Coral Pillow Depot Website

Need a design for a local Miami mattress store.
The store is called Coral Pillow Depot.
need it to be something that customers can find on the internet and will
give them my location, they need to know i have the same brand mattress as the other store except i have them at almost half the price.

the office phone number is (786)555-0147
the office address is: 4721 sw Heron Glade Ave, Miami FL 33190

included is the logo, id like to stick the with white and teal design

here are is an excerpt that can or cannot be included

"We are a premium mattress discount outlet store located in South Florida; offering Free Delivery to Broward Miami-Dade, the Keys, and Palm Beach.

We carry the best brands in the market: Harlow DreamNest; Brovik SpineEase, Kendal & Pryce, Tarvin, among others.

We are open 7 days a week, and we are accessible from all major highways. We are a family business and our goal is to provide you with the most comfortable and best quality mattress at a price that has no competition. Come visit us and take a look at our large inventory selection."

```html
<!DOCTYPE html>
<html lang="en">
<head>
<meta charset="utf-8">
<title>Coral Pillow Depot</title>
<link href="https://fonts.googleapis.com/css2?family=Open+Sans:wght@400;600;700&display=swap" rel="stylesheet">
<style>
:root{
  --teal:#1ea6c8;
  --teal-dark:#15869f;
  --teal-light:#d7f0f7;
  --ink:#333b40;
  --muted:#7b8489;
  --line:#e3e6e8;
  --field:#dcdfe1;
  --footer:#2f3235;
  --footer-deep:#222426;
  --white:#ffffff;
}
*{box-sizing:border-box;margin:0;padding:0}
html,body{width:692px;height:1200px;overflow:hidden;background:var(--white)}
body{font-family:"Open Sans",Arial,sans-serif;color:var(--ink);font-size:8px;line-height:1.45}
.page{width:692px;height:1200px;position:relative}

/* header */
.site-header{height:66px;display:flex;align-items:center;justify-content:space-between;padding:0 40px}
.brand{display:flex;align-items:center;gap:8px}
.brand-mark{width:14px;height:14px;border-radius:50%;background:var(--teal)}
.brand-name{font-size:19px;font-weight:600;color:var(--ink);letter-spacing:.3px}
.header-contacts{display:flex;gap:18px}
.header-contact{display:flex;align-items:center;gap:6px}
.header-contact .icon{width:20px;height:20px;border-radius:50%;background:var(--teal);display:flex;align-items:center;justify-content:center}
.header-contact small{display:block;font-size:7px;color:var(--muted)}
.header-contact strong{display:block;font-size:9px;font-weight:600;color:var(--ink)}

/* nav */
.main-nav{height:26px;background:var(--teal);display:flex;align-items:center;justify-content:space-between;padding:0 40px}
.nav-links{display:flex;height:100%}
.nav-links a{color:var(--white);text-decoration:none;font-size:9px;font-weight:600;padding:0 14px;display:flex;align-items:center}
.nav-links a.active{background:var(--white);color:var(--ink)}
.nav-search{width:130px;height:15px;background:var(--white);border-radius:2px;display:flex;align-items:center;justify-content:space-between;padding:0 5px;font-size:7px;color:var(--muted)}

/* hero */
.hero{height:282px;position:relative;border-bottom:4px solid var(--teal)}
.hero-photo{position:absolute;inset:0;background:linear-gradient(180deg,#d9d3c8 0%,#c2b49f 40%,#ece8e2 70%,#cfc6b8 100%)}
.hero-tagline{position:absolute;left:0;right:0;top:106px;text-align:center;font-size:17px;color:var(--white);background:rgba(30,166,200,.55);padding:6px 0}
.hero-dots{position:absolute;right:40px;bottom:10px;display:flex;gap:5px}
.hero-dots span{width:8px;height:8px;border-radius:50%;background:rgba(255,255,255,.6)}
.hero-dots span.on{background:var(--teal)}

/* features */
.features{display:flex;gap:21px;padding:22px 40px 0;height:208px}
.feature{flex:1}
.feature h2{font-size:14px;font-weight:700;margin-bottom:6px}
.feature h2 span{color:var(--teal)}
.feature-photo{height:76px;border:3px solid var(--line);background:linear-gradient(135deg,#f3efe6,#d9d2c4)}
.feature-lead{color:var(--teal);font-weight:600;font-size:7px;margin-top:6px}
.feature p{font-size:7px;color:var(--muted)}
.btn{display:inline-block;background:var(--teal);color:var(--white);font-size:7px;font-weight:600;padding:3px 9px;border-radius:2px;margin-top:5px}

/* welcome */
.welcome{height:136px;text-align:center;padding:10px 70px 0;border-top:1px solid var(--line)}
.section-title{display:flex;align-items:center;justify-content:center;gap:10px;font-size:14px;font-weight:700}
.section-title .slash{width:14px;height:14px}
.section-title em{font-style:normal;color:var(--teal)}
.welcome .lead{font-weight:700;font-size:8px;margin-top:4px}
.welcome p{font-size:7px;color:var(--muted);margin-top:6px}

/* services */
.services{height:186px;background:var(--teal);padding:18px 40px;display:flex;gap:40px}
.services-list{flex:1}
.services .section-title{justify-content:flex-start;color:var(--white)}
.service-grid{display:grid;grid-template-columns:1fr 1fr;gap:14px 20px;margin-top:18px}
.service{display:flex;align-items:center;gap:8px;color:var(--white);font-size:8px;font-weight:600}
.service .icon{width:20px;height:20px;border-radius:50%;border:1px solid rgba(255,255,255,.7);display:flex;align-items:center;justify-content:center}
.service-video{width:215px;height:128px;margin-top:12px;border:4px solid var(--white);background:linear-gradient(160deg,#e9e4da,#b9ab94);position:relative}
.service-video .play{position:absolute;left:50%;top:50%;transform:translate(-50%,-50%)}

/* contact */
.contact{height:180px;display:flex;gap:24px;padding:14px 40px 0}
.contact h3{font-size:11px;font-weight:700;border-bottom:1px solid var(--line);padding-bottom:5px;margin-bottom:8px}
.quick-contact{width:200px}
.field{height:15px;background:var(--field);margin-bottom:5px;font-size:7px;color:var(--muted);padding:2px 6px}
.field.area{height:32px}
.contact-info{flex:1}
.info-row{display:flex;align-items:center;gap:8px;margin-bottom:6px;font-size:7px}
.info-row .icon{width:18px;height:18px;border-radius:50%;background:var(--teal);display:flex;align-items:center;justify-content:center;flex:none}
.info-row strong{font-size:10px;font-weight:600}
.contact-map{width:150px;height:150px;border-radius:50%;background:radial-gradient(circle at 40% 40%,#eef0ea,#cfd8cf);border:4px solid var(--line);align-self:center}

/* footer */
.site-footer{height:72px;background:var(--footer);display:flex;justify-content:space-between;padding:10px 40px;color:var(--white)}
.site-footer h4{font-size:9px;font-weight:700;margin-bottom:8px}
.newsletter-form{display:flex}
.newsletter-form .input{width:120px;height:16px;background:var(--white);font-size:7px;color:var(--muted);padding:3px 5px}
.newsletter-form .go{height:16px;background:var(--teal);font-size:7px;font-weight:700;padding:3px 7px}
.card-row,.social-row{display:flex;gap:5px}
.card-row span{width:26px;height:16px;background:#e6e8ea;border-radius:2px}
.social-row span{width:18px;height:18px;border-radius:50%;background:var(--white)}
.copyright{height:22px;background:var(--footer-deep);color:#9aa2a6;font-size:7px;display:flex;align-items:center;justify-content:center}
</style>
</head>
<body>
<div class="page">

<header class="site-header">
  <div class="brand"><span class="brand-mark"></span><span class="brand-name">Coral Pillow Depot</span></div>
  <div class="header-contacts">
    <div class="header-contact">
      <span class="icon"><svg width="10" height="10" viewBox="0 0 10 10"><path d="M2 1l2 2-1 1.3c.6 1.2 1.5 2.1 2.7 2.7L7 6l2 2-1.3 1.3C4.6 9 1 5.4.7 2.3z" fill="#fff"/></svg></span>
      <div><small>Call Now</small><strong>(786)555-0147</strong></div>
    </div>
    <div class="header-contact">
      <span class="icon"><svg width="10" height="8" viewBox="0 0 10 8"><rect x=".5" y=".5" width="9" height="7" fill="none" stroke="#fff"/><path d="M.5 .5L5 4.5 9.5.5" fill="none" stroke="#fff"/></svg></span>
      <div><small>Email Us</small><strong>info@coralpillowdepot.com</strong></div>
    </div>
  </div>
</header>

<nav class="main-nav">
  <div class="nav-links">
    <a class="active">Home</a><a>About</a><a>Products</a><a>Services</a><a>Location</a><a>Contact</a>
  </div>
  <div class="nav-search">Search
    <svg width="8" height="8" viewBox="0 0 8 8"><circle cx="3.3" cy="3.3" r="2.5" fill="none" stroke="#7b8489"/><path d="M5.2 5.2L7.5 7.5" stroke="#7b8489"/></svg>
  </div>
</nav>

<section class="hero">
  <div class="hero-photo" role="img" aria-label="Bright bedroom with a made-up mattress, lamp and flowers"></div>
  <p class="hero-tagline">We will not burn a hole in your pocket</p>
  <div class="hero-dots"><span class="on"></span><span></span><span></span><span></span></div>
</section>

<section class="features">
  <article class="feature">
    <h2>Natural <span>Latex</span></h2>
    <div class="feature-photo" role="img" aria-label="Close-up of a natural latex mattress layer"></div>
    <p class="feature-lead">Sed diam nonummy nibh euismod</p>
    <p>Lorem ipsum dolor sit amet, consectetuer adipiscing elit sed diam nonummy nibh.</p>
    <span class="btn">Read More</span>
  </article>
  <article class="feature">
    <h2>Memory <span>Foam</span></h2>
    <div class="feature-photo" role="img" aria-label="Hand pressing into memory foam"></div>
    <p class="feature-lead">Sed diam nonummy nibh euismod</p>
    <p>Lorem ipsum dolor sit amet, consectetuer adipiscing elit sed diam nonummy nibh.</p>
    <span class="btn">Read More</span>
  </article>
  <article class="feature">
    <h2>Coil <span>Support</span></h2>
    <div class="feature-photo" role="img" aria-label="Cutaway view of mattress coil springs"></div>
    <p class="feature-lead">Sed diam nonummy nibh euismod</p>
    <p>Lorem ipsum dolor sit amet, consectetuer adipiscing elit sed diam nonummy nibh.</p>
    <span class="btn">Read More</span>
  </article>
</section>

<section class="welcome">
  <h2 class="section-title">
    <svg class="slash" viewBox="0 0 14 14"><path d="M4 13L9 1M8 13L13 1" stroke="#1ea6c8" stroke-width="1.5"/></svg>
    <span>Welcome to <em>Coral Pillow Depot</em></span>
    <svg class="slash" viewBox="0 0 14 14"><path d="M1 13L6 1M5 13L10 1" stroke="#1ea6c8" stroke-width="1.5"/></svg>
  </h2>
  <p class="lead">Lorem ipsum dolor sit amet, consectetuer adipiscing elit sed diam nonummy</p>
  <p>Ut wisi enim ad minim veniam, quis nostrud exerci tation ullamcorper suscipit lobortis nisl ut aliquip ex ea commodo consequat. Duis autem vel eum iriure dolor in hendrerit in vulputate velit esse molestie consequat, vel illum dolore eu feugiat nulla facilisis at vero eros et accumsan et iusto odio dignissim qui blandit praesent luptatum zzril delenit augue duis dolore te feugait nulla facilisi.</p>
  <span class="btn">Read More</span>
</section>

<section class="services">
  <div class="services-list">
    <h2 class="section-title"><span>Our Services</span>
      <svg class="slash" viewBox="0 0 14 14"><path d="M1 13L6 1M5 13L10 1" stroke="#fff" stroke-width="1.5"/></svg>
    </h2>
    <div class="service-grid">
      <div class="service"><span class="icon"><svg width="10" height="8" viewBox="0 0 10 8"><path d="M1 4l3 3 5-6" fill="none" stroke="#fff" stroke-width="1.4"/></svg></span>FREE DELIVERY</div>
      <div class="service"><span class="icon"><svg width="10" height="8" viewBox="0 0 10 8"><path d="M1 4l3 3 5-6" fill="none" stroke="#fff" stroke-width="1.4"/></svg></span>WE BEAT LOWER PRICES</div>
      <div class="service"><span class="icon"><svg width="10" height="8" viewBox="0 0 10 8"><path d="M1 4l3 3 5-6" fill="none" stroke="#fff" stroke-width="1.4"/></svg></span>OPEN 7 DAYS A WEEK</div>
      <div class="service"><span class="icon"><svg width="10" height="8" viewBox="0 0 10 8"><path d="M1 4l3 3 5-6" fill="none" stroke="#fff" stroke-width="1.4"/></svg></span>PROVIDE SPECIAL OFFER</div>
      <div class="service"><span class="icon"><svg width="10" height="8" viewBox="0 0 10 8"><path d="M1 4l3 3 5-6" fill="none" stroke="#fff" stroke-width="1.4"/></svg></span>100% GUARANTEE</div>
      <div class="service"><span class="icon"><svg width="10" height="8" viewBox="0 0 10 8"><path d="M1 4l3 3 5-6" fill="none" stroke="#fff" stroke-width="1.4"/></svg></span>BEST BRANDS</div>
    </div>
  </div>
  <div class="service-video" role="img" aria-label="Video still of a bedroom showroom">
    <svg class="play" width="26" height="26" viewBox="0 0 26 26"><circle cx="13" cy="13" r="12" fill="rgba(0,0,0,.35)"/><path d="M10 8l8 5-8 5z" fill="#fff"/></svg>
  </div>
</section>

<section class="contact">
  <div class="quick-contact">
    <h3>Quick Contact</h3>
    <div class="field">Name</div>
    <div class="field">Email</div>
    <div class="field">Phone</div>
    <div class="field area">Message</div>
    <span class="btn">SUBMIT</span>
  </div>
  <div class="contact-info">
    <h3>Contact information</h3>
    <div class="info-row"><span class="icon"><svg width="10" height="10" viewBox="0 0 10 10"><circle cx="5" cy="5" r="4" fill="none" stroke="#fff"/><path d="M5 2.5V5h2" fill="none" stroke="#fff"/></svg></span><span>Mon to Sun: 9am to 7pm<br>After Hours By Appointment Only</span></div>
    <div class="info-row"><span class="icon"><svg width="8" height="10" viewBox="0 0 8 10"><path d="M4 10S.5 5.8.5 3.6a3.5 3.5 0 017 0C7.5 5.8 4 10 4 10z" fill="#fff"/><circle cx="4" cy="3.6" r="1.2" fill="#1ea6c8"/></svg></span><span>4721 sw Heron Glade Ave,<br>Miami FL 33190</span></div>
    <div class="info-row"><span class="icon"><svg width="10" height="10" viewBox="0 0 10 10"><path d="M2 1l2 2-1 1.3c.6 1.2 1.5 2.1 2.7 2.7L7 6l2 2-1.3 1.3C4.6 9 1 5.4.7 2.3z" fill="#fff"/></svg></span><strong>(786)555-0147</strong></div>
    <div class="info-row"><span class="icon"><svg width="10" height="10" viewBox="0 0 10 10"><path d="M2 1l2 2-1 1.3c.6 1.2 1.5 2.1 2.7 2.7L7 6l2 2-1.3 1.3C4.6 9 1 5.4.7 2.3z" fill="#fff"/></svg></span><strong>(786)555-0147</strong></div>
    <div class="info-row"><span class="icon"><svg width="10" height="8" viewBox="0 0 10 8"><rect x=".5" y=".5" width="9" height="7" fill="none" stroke="#fff"/><path d="M.5 .5L5 4.5 9.5.5" fill="none" stroke="#fff"/></svg></span><span>info@coralpillowdepot.com</span></div>
  </div>
  <div class="contact-map" role="img" aria-label="Street map around the store location"></div>
</section>

<footer class="site-footer">
  <div>
    <h4>Newsletter Signup</h4>
    <div class="newsletter-form"><span class="input">Enter email here</span><span class="go">GO</span></div>
  </div>
  <div>
    <h4>We Accept</h4>
    <div class="card-row"><span></span><span></span><span></span><span></span></div>
  </div>
  <div>
    <h4>Stay in Touch</h4>
    <div class="social-row"><span></span><span></span><span></span><span></span></div>
  </div>
</footer>
<div class="copyright">Copyright © 2014 Coral Pillow Depot &nbsp;|&nbsp; Terms and conditions</div>

</div>
</body>
</html>
```